Pruett Family Motto/Mission Statement

We are creating a poster to be hung in our home with several purpose statements for our family (last name Pruett, and "The Pruett Family" should be included in the poster prominently). The text that we want included is in the attached file.

Our kids range in age from 8 to 17, so we are looking for something that is homey and cheerful, but fairly bold and oriented to older kids (and not so much younger kids).

I've attached a couple of example poster/statements that we generally like. Overall color scheme could include blues and greens and possibly some brown.

Anticipated size of this poster would be 18"x24" with a portrait orientation.

```html
<!DOCTYPE html>
<html lang="en">
<head>
<meta charset="utf-8">
<title>The Pruett Family – Family Statement Poster</title>
<link rel="stylesheet" href="https://fonts.googleapis.com/css2?family=Bebas+Neue&family=Raleway:wght@300;400;800&display=swap">
<style>
  :root {
    --stage: #d9d9d9;
    --sky-top: #262838;
    --sky-mid: #4e5060;
    --haze: #6a6a72;
    --earth: #6e4c36;
    --earth-deep: #4a3122;
    --panel: rgba(255, 255, 255, 0.13);
    --panel-edge: rgba(255, 255, 255, 0.18);
    --ink: #f4f4f6;
    --rule: rgba(255, 255, 255, 0.75);
    --learn: #2d5aa6;
    --positive: #3b82cc;
    --kindness: #d8405f;
    --adventure: #5cc59b;
    --fit: #27508f;
    --humor: #86c9cf;
    --right: #f3b700;
  }

  * { margin: 0; padding: 0; box-sizing: border-box; }

  html, body {
    width: 1200px;
    height: 900px;
    overflow: hidden;
    background: var(--stage);
  }

  .poster {
    position: absolute;
    left: 394px;
    top: 123px;
    width: 461px;
    height: 615px;
    overflow: hidden;
    box-shadow: 0 6px 28px rgba(0, 0, 0, 0.45);
  }

  .poster__backdrop {
    position: absolute;
    inset: 0;
    background:
      radial-gradient(ellipse 40% 30% at 50% 58%, rgba(150, 110, 80, 0.55), transparent 70%),
      linear-gradient(180deg,
        var(--sky-top) 0%,
        var(--sky-mid) 35%,
        var(--haze) 62%,
        var(--earth) 80%,
        var(--earth-deep) 100%);
  }

  .poster__panel {
    position: absolute;
    left: 41px;
    top: 35px;
    width: 380px;
    height: 537px;
    border-radius: 10px;
    background: var(--panel);
    border: 1px solid var(--panel-edge);
  }

  .poster__rule {
    position: absolute;
    left: 103px;
    width: 255px;
    height: 1px;
    background: var(--rule);
  }
  .poster__rule--top { top: 63px; }
  .poster__rule--bottom { top: 538px; }

  .poster__dot {
    position: absolute;
    top: 91px;
    width: 10px;
    height: 10px;
    border-radius: 50%;
    background: var(--ink);
  }
  .poster__dot--left { left: 69px; }
  .poster__dot--right { left: 379px; }

  .poster__title {
    position: absolute;
    left: 0;
    right: 0;
    top: 73px;
    text-align: center;
    font-family: "Bebas Neue", "Oswald", sans-serif;
    font-size: 46px;
    line-height: 48px;
    color: #ffffff;
    text-shadow: 0 0 8px rgba(255, 255, 255, 0.45);
    letter-spacing: -0.5px;
  }

  .statement {
    position: absolute;
    left: 0;
    right: 0;
    text-align: center;
    font-family: "Raleway", "Helvetica Neue", sans-serif;
    font-weight: 400;
    font-size: 16.5px;
    line-height: 22px;
    color: var(--ink);
    text-transform: uppercase;
    letter-spacing: -0.2px;
    text-shadow: 0 0 4px rgba(0, 0, 0, 0.35);
  }

  .value {
    font-weight: 800;
    text-shadow:
      1px 0 0 #fff, -1px 0 0 #fff, 0 1px 0 #fff, 0 -1px 0 #fff,
      1px 1px 0 #fff, -1px -1px 0 #fff, 1px -1px 0 #fff, -1px 1px 0 #fff,
      0 0 6px rgba(255, 255, 255, 0.6);
  }
  .value--learn { color: var(--learn); }
  .value--positive { color: var(--positive); }
  .value--kindness { color: var(--kindness); }
  .value--adventure { color: var(--adventure); }
  .value--fit { color: var(--fit); }
  .value--humor { color: var(--humor); }
  .value--right { color: var(--right); }
</style>
</head>
<body>
  <main class="poster">
    <div class="poster__backdrop" role="img" aria-label="Photograph of a desert butte under a starry night sky"></div>
    <div class="poster__panel"></div>

    <div class="poster__rule poster__rule--top"></div>
    <span class="poster__dot poster__dot--left"></span>
    <h1 class="poster__title">The Pruett Family</h1>
    <span class="poster__dot poster__dot--right"></span>

    <p class="statement" style="top:127px">We love to <span class="value value--learn">learn</span> new things</p>
    <p class="statement" style="top:161px">We look at life through a <span class="value value--positive">positive</span> lens</p>

    <p class="statement" style="top:218px"><span class="value value--kindness">Kindness</span> guides our words and deeds</p>
    <p class="statement" style="top:250px">We create <span class="value value--adventure">adventure</span> and choose</p>
    <p class="statement" style="top:283px">experiences over things</p>

    <p class="statement" style="top:335px">We commit to be <span class="value value--fit">fit</span></p>
    <p class="statement" style="top:368px">Our days are brightened by a</p>
    <p class="statement" style="top:403px"><span class="value value--humor">Sense of humor</span></p>

    <p class="statement" style="top:458px">We <span class="value value--right">do what is right</span></p>
    <p class="statement" style="top:491px">even when no one is waiting</p>

    <div class="poster__rule poster__rule--bottom"></div>
  </main>
</body>
</html>
```